Commerical Office Furniture Company Needs Truck Wrap Design for Box Truck

We need a truck wrap design (and business card) for our company based in Fresno, California. We offer commercial office furnishings such as private office desks, cubicle stations, conference tables, all office seating (task chairs, guest, lobby/lounge, conference) storage systems, ergonomic solutions (monitor arms, keyboard trays, lift desks) and much more. We are a full service office furniture dealer who can fully outfit every space and need for a new or existing office space. We also offer design and space planning services and professional installation.
We would like our trap wrap to be modern using the same color scheme as our logo with a clean but eye catching look. Perhaps using a few nice looking desk/workstations product images as examples to show people what we are capable of. We attached some examples of some themes/layouts we like. feel free to be creative. Our website tembrolight.com has some images and info.
https://imagelibrary.brv-corp.com/detail/client-space-shared-prism-workstation-with-t-line-storage-height-adjustable-tables-and-dorval-seating
Target Market(s)
Private Sector, Education, Healthcare
Industry/Entity Type
Requirements
Must have
- Varto Box Truck - 190 inches x 85 inches

```html
<!DOCTYPE html>
<html lang="en">
<head>
<meta charset="utf-8">
<title>Tembrolight Office Interiors – Box Truck Wrap</title>
<link href="https://fonts.googleapis.com/css2?family=Archivo:wght@700;800&family=Montserrat:wght@400;700&display=swap" rel="stylesheet">
<style>
  :root{
    --brand-blue:#0057e7;
    --ink:#3a3d42;
    --panel:#ececee;
    --white:#ffffff;
    --page:#f7f7f8;
    --photo-light:#d9d3c9;
    --photo-dark:#8c7f70;
  }
  html,body{margin:0;padding:0;width:708px;height:1200px;overflow:hidden;background:var(--page);}
  .canvas{position:relative;width:708px;height:1200px;}
  .wrap-side{position:absolute;left:24px;top:80px;width:660px;height:278px;}
  .wrap-rear{position:absolute;left:54px;top:430px;width:600px;height:668px;}
  .brand-name{font-family:"Archivo",sans-serif;font-weight:800;fill:var(--brand-blue);}
  .brand-sub{font-family:"Archivo",sans-serif;font-weight:700;fill:var(--ink);}
  .services{font-family:"Archivo",sans-serif;font-weight:700;fill:var(--ink);}
  .contact{font-family:"Montserrat",sans-serif;fill:var(--white);}
  .contact .strong{font-weight:700;}
  .contact .light{font-weight:400;}
  .hex-halo{fill:var(--white);stroke:var(--white);stroke-width:26;stroke-linejoin:round;}
  .hex-photo{stroke:var(--brand-blue);stroke-width:2.5;}
  .band{fill:var(--brand-blue);}
  .rule{fill:var(--ink);}
</style>
</head>
<body>
<div class="canvas">

  <!-- Side panel -->
  <svg class="wrap-side" viewBox="0 0 950 400" aria-label="Truck side wrap">
    <defs>
      <linearGradient id="photoTone" x1="0" y1="0" x2="0" y2="1">
        <stop offset="0" stop-color="var(--photo-light)"/>
        <stop offset="1" stop-color="var(--photo-dark)"/>
      </linearGradient>
      <polygon id="s-a" points="465,53 501.4,74 501.4,116 465,137 428.6,116 428.6,74"/>
      <polygon id="s-b" points="635,78 658.4,91.5 658.4,118.5 635,132 611.6,118.5 611.6,91.5"/>
      <polygon id="s-c" points="555,115 628.6,157.5 628.6,242.5 555,285 481.4,242.5 481.4,157.5"/>
      <polygon id="s-d" points="693.6,125 758.6,162.5 758.6,237.5 693.6,275 628.6,237.5 628.6,162.5"/>
      <polygon id="s-e" points="850,147 908.9,181 908.9,249 850,283 791.1,249 791.1,181"/>
      <polygon id="s-f" points="465,252 506.6,276 506.6,324 465,348 423.4,324 423.4,276"/>
      <polygon id="s-g" points="545,288 571,303 571,333 545,348 519,333 519,303"/>
    </defs>
    <rect width="950" height="400" fill="var(--panel)"/>
    <path class="band" d="M0 283 H420 L440 330 L560 320 L650 275 L760 270 L950 160 V400 H0 Z"/>
    <rect class="rule" x="0" y="263" width="400" height="6"/>

    <text class="brand-name" x="205" y="118" font-size="44" text-anchor="middle">TEMBROLIGHT</text>
    <text class="brand-sub" x="205" y="172" font-size="20" text-anchor="middle" letter-spacing="5">— OFFICE INTERIORS —</text>
    <text class="services" x="205" y="207" font-size="15" text-anchor="middle">Office Furniture  •  Design  •  Installation</text>

    <g class="hex-halo">
      <use href="#s-a"/><use href="#s-b"/><use href="#s-c"/><use href="#s-d"/>
      <use href="#s-e"/><use href="#s-f"/><use href="#s-g"/>
    </g>
    <g class="hex-photo" fill="url(#photoTone)">
      <use href="#s-a" role="img" aria-label="Photo of a private office desk with task chair"/>
      <use href="#s-b" role="img" aria-label="Photo of a small office workspace"/>
      <use href="#s-c" role="img" aria-label="Photo of a conference room with a wood table and chairs, left half"/>
      <use href="#s-d" role="img" aria-label="Photo of a conference room with a wood table and chairs, right half"/>
      <use href="#s-e" role="img" aria-label="Photo of a reception desk workstation"/>
      <use href="#s-f" role="img" aria-label="Photo of cubicle workstations"/>
      <use href="#s-g" role="img" aria-label="Photo of a storage cabinet"/>
    </g>

    <g class="contact">
      <circle cx="50" cy="318" r="15" fill="var(--white)"/>
      <path d="M43 310 q2 -3 5 0 l2 4 q1 2 -1 3 l-1 1 q2 4 6 6 l1 -1 q1 -2 3 -1 l4 2 q3 3 0 5 q-3 3 -8 1 q-9 -4 -12 -13 q-2 -5 1 -7z" fill="var(--brand-blue)"/>
      <text class="strong" x="75" y="332" font-size="38">555-014-2290</text>
      <circle cx="50" cy="368" r="14" fill="none" stroke="var(--white)" stroke-width="2.5"/>
      <ellipse cx="50" cy="368" rx="6" ry="14" fill="none" stroke="var(--white)" stroke-width="2"/>
      <line x1="36" y1="368" x2="64" y2="368" stroke="var(--white)" stroke-width="2"/>
      <text x="75" y="381" font-size="34"><tspan class="strong">tembrolight</tspan><tspan class="light">.com</tspan></text>
    </g>
  </svg>

  <!-- Rear doors -->
  <svg class="wrap-rear" viewBox="0 0 575 640" aria-label="Truck rear wrap">
    <defs>
      <linearGradient id="photoToneRear" x1="0" y1="0" x2="0" y2="1">
        <stop offset="0" stop-color="var(--photo-light)"/>
        <stop offset="1" stop-color="var(--photo-dark)"/>
      </linearGradient>
      <clipPath id="rearPanel"><rect x="40" y="55" width="495" height="575"/></clipPath>
      <polygon id="r-a" points="95,260 129.6,280 129.6,320 95,340 60.4,320 60.4,280"/>
      <polygon id="r-b" points="260,274 282.5,287 282.5,313 260,326 237.5,313 237.5,287"/>
      <polygon id="r-c" points="180,322 247.5,361 247.5,439 180,478 112.5,439 112.5,361"/>
      <polygon id="r-d" points="308.1,330 368.7,365 368.7,435 308.1,470 247.5,435 247.5,365"/>
      <polygon id="r-e" points="455,342 513.9,376 513.9,444 455,478 396.1,444 396.1,376"/>
      <polygon id="r-f" points="95,457 136.6,481 136.6,529 95,553 53.4,529 53.4,481"/>
      <polygon id="r-g" points="185,497 209.2,511 209.2,539 185,553 160.8,539 160.8,511"/>
    </defs>
    <rect width="575" height="640" rx="6" fill="var(--brand-blue)"/>
    <rect x="40" y="55" width="495" height="575" fill="var(--panel)"/>
    <g clip-path="url(#rearPanel)">
      <path class="band" d="M40 630 V560 L95 590 L230 515 L300 490 L390 500 L535 420 V630 Z"/>
      <g class="hex-halo">
        <use href="#r-a"/><use href="#r-b"/><use href="#r-c"/><use href="#r-d"/>
        <use href="#r-e"/><use href="#r-f"/><use href="#r-g"/>
      </g>
    </g>

    <text class="brand-name" x="287" y="148" font-size="50" text-anchor="middle">TEMBROLIGHT</text>
    <text class="brand-sub" x="287" y="208" font-size="21" text-anchor="middle" letter-spacing="5">— OFFICE INTERIORS —</text>
    <text class="services" x="287" y="238" font-size="14" text-anchor="middle">Office Furniture  •  Design  •  Installation</text>

    <g class="hex-photo" fill="url(#photoToneRear)">
      <use href="#r-a" role="img" aria-label="Photo of a private office desk with task chair"/>
      <use href="#r-b" role="img" aria-label="Photo of a small office workspace"/>
      <use href="#r-c" role="img" aria-label="Photo of a conference room with a wood table and chairs, left half"/>
      <use href="#r-d" role="img" aria-label="Photo of a conference room with a wood table and chairs, right half"/>
      <use href="#r-e" role="img" aria-label="Photo of a reception desk workstation"/>
      <use href="#r-f" role="img" aria-label="Photo of cubicle workstations"/>
      <use href="#r-g" role="img" aria-label="Photo of a storage cabinet"/>
    </g>

    <g class="contact">
      <g transform="translate(10 0)">
        <circle cx="287" cy="542" r="11" fill="var(--white)"/>
        <path d="M282 536 q1.5 -2 3.5 0 l1.5 3 q.7 1.5 -.7 2 l-.7 .7 q1.5 3 4.5 4.5 l.7 -.7 q.7 -1.5 2 -.7 l3 1.5 q2 2 0 3.5 q-2 2 -6 .7 q-6.5 -3 -8.8 -9.5 q-1.4 -3.5 1 -5z" fill="var(--brand-blue)"/>
      </g>
      <text class="strong" x="316" y="552" font-size="26">555-014-2290</text>
      <circle cx="324" cy="580" r="9" fill="none" stroke="var(--white)" stroke-width="2"/>
      <ellipse cx="324" cy="580" rx="4" ry="9" fill="none" stroke="var(--white)" stroke-width="1.5"/>
      <line x1="315" y1="580" x2="333" y2="580" stroke="var(--white)" stroke-width="1.5"/>
      <text x="340" y="588" font-size="21"><tspan class="strong">tembrolight</tspan><tspan class="light">.com</tspan></text>
    </g>
  </svg>

</div>
</body>
</html>
```